Large multi-office optometry business opening a Dry Eye Spa and needs sign.

Business name/sign info: Brindlecove Dry Eye Institute, (555) 316-4872
Backlit pole sign at office entrance on a very busy street
Sign dimensions: 53" tall x 136.5" wide
State of the art Dry Eye Spa for treatment of all forms of dry eye and ocular surface disease. Also, have aesthetics treatments (IPL, Low Level Light Treatment, etc.)

Target Market(s)

People who are suffering from: dryness, burning, foreign body sensation, itching, fluctuating vision, tired eyes, etc.

Industry/Entity Type

Optometry and aesthetics

Colors
0054AA
0677BA
7BADD7
CADEEF
E8F1F8

Requirements
Must have
• Business name, phone number, subliminal message of relief in a glance or short look.
Nice to have
• Cool, relief, soothing sense.
Should not have
• Too much information or too busy.

```html
<!DOCTYPE html>
<html lang="en">
<head>
<meta charset="utf-8">
<title>Brindlecove Dry Eye Institute – Pole Sign</title>
<link href="https://fonts.googleapis.com/css2?family=Oswald:wght@500;600;700&family=Poppins:wght@600;700&display=swap" rel="stylesheet">
<style>
  :root {
    --navy: #003a70;
    --blue: #0054aa;
    --blue-mid: #0677ba;
    --red: #c8252c;
    --white: #ffffff;
    --stage: #e6e9ec;
    --skin-light: #f0c9a8;
    --skin-mid: #d49a72;
    --skin-dark: #8a5a3c;
    --iris: #9fb4d2;
  }
  * { box-sizing: border-box; margin: 0; padding: 0; }
  html, body { width: 1013px; height: 1200px; overflow: hidden; }
  body { background: var(--stage); position: relative; }

  .sign {
    position: absolute;
    left: 26px; top: 413px;
    width: 960px; height: 374px;
    background: var(--white);
    box-shadow: 0 10px 28px rgba(0,0,0,.28);
    overflow: hidden;
  }
  .sign__photo {
    position: absolute;
    left: 0; top: 0;
    width: 352px; height: 100%;
    background:
      radial-gradient(ellipse 90px 80px at 210px 195px, var(--iris) 0%, #c9d4e3 55%, rgba(240,232,226,0) 100%),
      linear-gradient(160deg, var(--skin-dark) 0%, var(--skin-mid) 38%, var(--skin-light) 70%, #f6dcc6 100%);
  }
  .sign__photo::after {
    content: "";
    position: absolute; right: -40px; top: 0;
    width: 80px; height: 100%;
    background: linear-gradient(90deg, rgba(255,255,255,0), var(--white));
  }
  .sign__content {
    position: absolute;
    left: 360px; right: 0; top: 0; bottom: 0;
    display: flex; flex-direction: column; align-items: center;
    padding-top: 30px;
  }
  .practice-name {
    font-family: "Poppins", sans-serif;
    font-weight: 600;
    font-size: 20px;
    line-height: 1.15;
    color: var(--blue-mid);
    text-align: center;
    margin-left: -40px;
  }
  .institute-name {
    font-family: "Oswald", sans-serif;
    font-weight: 700;
    font-size: 104px;
    line-height: 1;
    color: var(--navy);
    letter-spacing: -1px;
    margin-top: 6px;
  }
  .institute-tag {
    margin-top: 10px;
    background: var(--red);
    border-radius: 3px;
    padding: 4px 20px 5px;
    font-family: "Oswald", sans-serif;
    font-weight: 600;
    font-size: 32px;
    line-height: 1.1;
    letter-spacing: 3px;
    color: var(--white);
  }
  .phone {
    margin-top: 10px;
    font-family: "Poppins", sans-serif;
    font-weight: 700;
    font-size: 46px;
    line-height: 1.2;
    color: var(--blue);
  }
</style>
</head>
<body>
  <section class="sign">
    <div class="sign__photo" role="img" aria-label="Close-up photograph of a woman's open blue eye with long lashes"></div>
    <div class="sign__content">
      <p class="practice-name">Dr. Mara Pell's<br>Family Eye Care</p>
      <h1 class="institute-name">Brindlecove</h1>
      <p class="institute-tag">DRY EYE INSTITUTE</p>
      <p class="phone">(555) 316-4872</p>
    </div>
  </section>
</body>
</html>
```